Presntation folder
Larkvale Home Health Care
The Care you Deserve
we need a design for a presentation folder that would work with our logo design(done in the past by the brand mark foundry)
If you can incorporate this gold seal and text in your design
(Larkvale Home Health has earned the Meridane Council Azure Crest of Merit)

```html
<!DOCTYPE html>
<html lang="en">
<head>
<meta charset="utf-8">
<title>Larkvale Home Health Care – Presentation Folder</title>
<link rel="stylesheet" href="https://fonts.googleapis.com/css2?family=PT+Sans:wght@400;700&display=swap">
<style>
  :root {
    --navy: #0b2a5b;
    --green: #7cc242;
    --white: #ffffff;
    --paper: #ffffff;
    --gold-light: #f3d35a;
    --gold-dark: #c8951b;
    --cut: #8fa2c2;
  }
  html, body {
    margin: 0;
    width: 1200px;
    height: 901px;
    overflow: hidden;
    background: var(--paper);
  }
  .folder-dieline {
    display: block;
    width: 1200px;
    height: 901px;
    font-family: "PT Sans", "Myriad Pro", sans-serif;
  }
  .panel { fill: var(--navy); }
  .stripe, .pocket-rule { fill: var(--green); }
  .cut-line { stroke: var(--cut); stroke-width: 1; stroke-dasharray: 4 3; fill: none; }
  .slot { fill: var(--paper); }
  .brand-name { fill: var(--white); font-weight: 700; font-size: 40px; }
  .brand-tagline { fill: var(--green); font-weight: 400; font-size: 17px; }
  .brand-dot { fill: var(--green); }
  .hq-title { fill: var(--white); font-weight: 700; font-size: 13px; letter-spacing: 0.2px; }
  .hq-line { fill: var(--white); font-weight: 400; font-size: 11px; }
</style>
</head>
<body>
<svg class="folder-dieline" viewBox="0 0 1200 901" xmlns="http://www.w3.org/2000/svg">
  <defs>
    <radialGradient id="crest-fill" cx="40%" cy="35%" r="70%">
      <stop offset="0%" stop-color="var(--gold-light)"/>
      <stop offset="100%" stop-color="var(--gold-dark)"/>
    </radialGradient>
  </defs>

  <!-- folder body: back cover (left) and front cover (right) -->
  <rect class="panel" x="168" y="77" width="864" height="614"/>

  <!-- business-card slots -->
  <rect class="slot" x="168" y="372" width="29" height="132"/>
  <rect class="slot" x="1003" y="372" width="29" height="132"/>

  <!-- inside pocket flap -->
  <g class="pocket">
    <rect class="panel" x="144" y="691" width="912" height="125"/>
    <rect class="pocket-rule" x="144" y="691" width="912" height="7"/>
    <polygon class="slot" points="590,691 610,691 629,816 571,816"/>
    <line class="cut-line" x1="168" y1="698" x2="168" y2="816"/>
    <line class="cut-line" x1="1032" y1="698" x2="1032" y2="816"/>
    <line class="cut-line" x1="168" y1="708" x2="590" y2="708"/>
    <line class="cut-line" x1="612" y1="708" x2="1032" y2="708"/>
  </g>

  <!-- spine stripes -->
  <g class="spine-stripes">
    <rect class="stripe" x="600" y="77" width="34" height="614"/>
    <rect class="stripe" x="648" y="77" width="29" height="614"/>
    <rect class="stripe" x="691" y="77" width="10" height="614"/>
    <rect class="stripe" x="708" y="77" width="7" height="614"/>
    <rect class="stripe" x="722" y="77" width="8" height="614"/>
    <rect class="stripe" x="735" y="77" width="3" height="614"/>
    <rect class="stripe" x="744" y="77" width="3" height="614"/>
  </g>

  <!-- front cover brand name -->
  <g class="brand">
    <circle class="brand-dot" cx="808" cy="170" r="20"/>
    <text class="brand-name" x="838" y="184">Larkvale</text>
    <text class="brand-tagline" x="839" y="204">Home Health Care</text>
  </g>

  <!-- accreditation crest -->
  <circle cx="925" cy="650" r="32" fill="url(#crest-fill)" role="img" aria-label="Meridane Council Azure Crest of Merit seal"/>

  <!-- back cover headquarters block -->
  <g class="hq-contact">
    <text class="hq-title" x="320" y="613">LARKVALE HHC HEADQUARTER</text>
    <text class="hq-line" x="320" y="630">1280 Orchard Crest Drive, Suite 210</text>
    <text class="hq-line" x="320" y="644">Brookmere, MI 48977</text>
    <text class="hq-line" x="320" y="658">Phone: (555)014-2830</text>
    <text class="hq-line" x="320" y="672">Fax: (555)014-2831</text>
  </g>
</svg>
</body>
</html>
```